Business Card Design Project

We need a business card design for a consultancy called 'Maple Ridge'. The design should communicate innovation and professionalism. The colors used should complement our logo. Please include source files for winning design.
Updates

Industry/Entity Type

Business

Colors

Designer to choose colors to be used in the design.

Requirements
Must have
• Card size should be 85mm x 50mm. The back side of the card should be the logo on a black background. The front side should display the name 'Maple Ridge' along with standard information. The front's design should graphically complement the back.
Nice to have
• Any graphical elements in the front the complement the back side (with the logo on a black background) would be a plus.

```html
<!DOCTYPE html>
<html lang="en">
<head>
<meta charset="utf-8">
<title>Maple Ridge — Business Card</title>
<link href="https://fonts.googleapis.com/css2?family=Cinzel:wght@600&family=Questrial&display=swap" rel="stylesheet">
<style>
  :root {
    --backdrop: #e8e5e0;
    --black: #0b0b0b;
    --orange: #f6a033;
    --orange-light: #fbb24a;
    --orange-deep: #e8561c;
    --accent-red: #ef4a24;
    --ink: #111111;
    --serif: "Cinzel", "Times New Roman", serif;
    --sans: "Questrial", "Century Gothic", sans-serif;
  }
  * { box-sizing: border-box; margin: 0; padding: 0; }
  html, body { width: 1200px; height: 784px; overflow: hidden; background: var(--backdrop); }
  .canvas { position: relative; width: 1200px; height: 784px; }

  .card {
    position: absolute;
    width: 620px; height: 365px;
    overflow: hidden;
    box-shadow: 0 6px 18px rgba(0,0,0,.25);
  }

  /* Back side */
  .card-back { left: 60px; top: 50px; background: var(--black); }
  .back-mark {
    position: absolute; left: 50%; top: 40px;
    width: 200px; height: 200px; margin-left: -100px;
    border-radius: 50%;
    background: var(--orange);
    border: 5px solid var(--orange-light);
  }
  .back-wordmark {
    position: absolute; left: 0; right: 0; top: 262px;
    text-align: center;
    font-family: var(--serif); font-weight: 600;
    font-size: 48px; letter-spacing: 1px;
    color: var(--orange);
  }

  /* Front side */
  .card-front { left: 520px; top: 380px; background: linear-gradient(135deg, var(--orange-light), var(--orange)); }
  .front-shape { position: absolute; inset: 0; }
  .front-mark {
    position: absolute; left: 410px; top: 40px;
    width: 180px; height: 180px;
    border-radius: 50%;
    background: var(--orange);
    border: 5px solid var(--orange-light);
  }
  .front-wordmark {
    position: absolute; left: 40px; top: 68px;
    font-family: var(--serif); font-weight: 600;
    font-size: 35px; color: var(--ink);
  }
  .person { position: absolute; left: 40px; top: 140px; font-family: var(--sans); }
  .person-name { font-size: 17px; color: var(--accent-red); }
  .person-role { font-size: 11px; color: var(--ink); margin-top: 2px; }

  .contacts {
    position: absolute; left: 40px; top: 218px;
    list-style: none;
    font-family: var(--sans); font-size: 15px; line-height: 17px;
    color: var(--ink);
  }
  .contacts li { display: flex; align-items: flex-start; gap: 5px; }
  .contacts svg { width: 13px; height: 13px; flex: none; margin-top: 2px; fill: none; stroke: var(--accent-red); stroke-width: 1.8; }
</style>
</head>
<body>
<div class="canvas">

  <section class="card card-back" aria-label="Card back">
    <div class="back-mark"></div>
    <div class="back-wordmark">Maple Ridge</div>
  </section>

  <section class="card card-front" aria-label="Card front">
    <svg class="front-shape" viewBox="0 0 620 365" width="620" height="365" aria-hidden="true">
      <path d="M268 0 H300 C360 180 470 290 620 300 V318 C450 310 330 190 268 0 Z" fill="var(--orange-deep)"/>
      <path d="M300 0 H620 V300 C470 290 360 180 300 0 Z" fill="var(--black)"/>
    </svg>
    <div class="front-mark"></div>

    <div class="front-wordmark">Maple Ridge</div>

    <div class="person">
      <div class="person-name">Nora Fielding</div>
      <div class="person-role">Manager</div>
    </div>

    <ul class="contacts">
      <li><svg viewBox="0 0 14 14"><rect x="3.5" y="1" width="7" height="12" rx="1"/><line x1="6" y1="11" x2="8" y2="11"/></svg>555-210-4817</li>
      <li><svg viewBox="0 0 14 14"><path d="M2 3 L4.5 1.5 L6.5 4.5 L5 6 C6 8 7 9 9 10 L10.5 8.5 L13 10.5 L11.5 12.5 C6 12 2.5 8 2 3 Z"/></svg>555-304-6621</li>
      <li><svg viewBox="0 0 14 14"><rect x="1.5" y="5.5" width="11" height="6" rx="1"/><rect x="4" y="1.5" width="6" height="4"/><line x1="4" y1="9" x2="10" y2="9"/></svg>555-304-6690</li>
      <li><svg viewBox="0 0 14 14"><rect x="1.5" y="3" width="11" height="8" rx="1"/><path d="M1.5 3.5 L7 8 L12.5 3.5"/></svg>hello@mapleridgemail.com</li>
      <li><svg viewBox="0 0 14 14"><circle cx="7" cy="7" r="5.5"/><ellipse cx="7" cy="7" rx="2.3" ry="5.5"/><line x1="1.5" y1="7" x2="12.5" y2="7"/></svg>www.mapleridge.com</li>
      <li><svg viewBox="0 0 14 14"><path d="M1.5 7 L7 2 L12.5 7"/><path d="M3.5 6 V12 H10.5 V6"/><rect x="6" y="8.5" width="2" height="3.5"/></svg>4810 N. Alder Road,<br>Linwood, CO 80000</li>
    </ul>
  </section>

</div>
</body>
</html>
```